Velmor Stationery Design

We need Business Card, Letterhead, #10 Envelope , 3" x 4" Mailing Label, and email signature block. Also need "Aircraft Services" added small under the logo on everything except the email signature block. "Aircraft Services" should be in a simple font to to conflict with or distract from the logo. Our address info is:
4817 Halvend Loop NW
Brantwick, GA 30592
P 555.208.3146
C 555.208.3146 (for biz cards only)
glen@velmorjet.example (for biz cards only)
Website velmorjet.example
Feel free to play around with colors but I expect that black or gray will work best for the address/phone info etc.

Target Market(s)

Aircraft owners

Industry/Entity Type

Aviation

Colors

Designer to choose only greyscale colors for use in the design.

Requirements
Must have
• Clean and sophisticated design -

```html
<!DOCTYPE html>
<html lang="en">
<head>
<meta charset="utf-8">
<title>Velmor Stationery</title>
<link href="https://fonts.googleapis.com/css2?family=Lato:wght@400;700;900&display=swap" rel="stylesheet">
<style>
  :root{
    --bg:#e6e7e9;
    --paper:#ffffff;
    --blue:#2e75bb;
    --charcoal:#434345;
    --ink:#3b3b3d;
    --muted:#6a6a6d;
    --window:#dcdcdd;
  }
  *{margin:0;padding:0;box-sizing:border-box}
  html,body{width:1200px;height:1200px;overflow:hidden;background:var(--bg)}
  body{position:relative;font-family:"Lato",sans-serif;color:var(--ink)}
  .piece{position:absolute;background:var(--paper);overflow:hidden}
  .wave{position:absolute;left:0;bottom:0;width:100%;display:block}
  .abs{position:absolute}

  /* Wordmark */
  .logo{position:absolute;display:flex;flex-direction:column;align-items:flex-end;line-height:1}
  .logo-name{font-family:"Lato",sans-serif;font-weight:900;color:var(--blue);letter-spacing:.04em;text-transform:uppercase}
  .logo-tag{font-family:"Lato",sans-serif;font-weight:400;color:var(--charcoal);letter-spacing:.28em;text-transform:uppercase;margin-top:.3em}
  .logo.on-blue .logo-name{color:#fff}
  .logo.on-blue .logo-tag{color:#fff}

  .icon{display:inline-block;vertical-align:middle;margin-right:4px}
  .contact-line{white-space:nowrap}

  /* Letterhead */
  .letterhead{left:40px;top:129px;width:510px;height:717px}
  .letterhead .logo{left:45px;top:44px}
  .letterhead .logo-name{font-size:30px}
  .letterhead .logo-tag{font-size:4.6px}
  .lh-address{left:365px;top:36px;border-left:1.5px solid var(--charcoal);padding-left:7px;font-size:9.6px;line-height:12.6px}
  .lh-address .gap{margin-top:3.5px}
  .lh-body{left:45px;top:163px;width:422px;font-size:9.4px;line-height:11px}
  .lh-body .date{margin-bottom:13px}
  .lh-body .block{margin-bottom:12px}
  .lh-body .salute{font-size:12.4px;margin:4px 0 9px}
  .lh-body p.copy{font-size:8.7px;line-height:10.9px;text-align:justify;margin-bottom:10.5px}
  .lh-regards{left:46px;top:496px;font-size:9px}
  .signature{left:46px;top:512px;width:130px;height:54px;background:linear-gradient(90deg,#eceef6,#f6f7fb);border-radius:4px}

  /* Envelope */
  .envelope{left:576px;top:161px;width:580px;height:374px;background:transparent}
  .env-flap{position:absolute;left:0;top:0;width:580px;height:83px;display:block}
  .env-body{position:absolute;left:0;top:82px;width:580px;height:292px;background:var(--paper);overflow:hidden}
  .envelope .logo{left:47px;top:42px}
  .envelope .logo-name{font-size:30px}
  .envelope .logo-tag{font-size:4.6px}
  .env-contact{left:47px;top:147px;font-size:9.4px;line-height:14.6px}
  .env-address{left:49px;top:197px;font-size:9.4px;line-height:13px}
  .env-window{left:332px;top:111px;width:186px;height:75px;background:var(--window);border-radius:6px}

  /* Business cards */
  .card-front{left:611px;top:578px;width:238px;height:137px;background:var(--blue)}
  .card-front .logo{left:58px;top:52px}
  .card-front .logo-name{font-size:27px}
  .card-front .logo-tag{font-size:4.2px}
  .card-back{left:862px;top:575px;width:238px;height:136px}
  .card-back .logo{left:21px;top:53px}
  .card-back .logo-name{font-size:19px}
  .card-back .logo-tag{font-size:3px}
  .cb-name{left:134px;top:33px;font-size:9px;font-weight:700;letter-spacing:.02em;color:var(--ink)}
  .cb-contact{left:134px;top:53px;font-size:5.4px;line-height:8.4px}
  .cb-address{left:136px;top:82px;font-size:5.4px;line-height:8.4px}

  /* Email signature */
  .email-sig{left:636px;top:785px;width:453px;height:151px}
  .email-sig .logo{left:32px;top:55px}
  .email-sig .logo-name{font-size:29px}
  .es-name{left:204px;top:48px;font-size:10.6px}
  .es-title{left:204px;top:62px;font-size:6px;color:var(--muted)}
  .es-rule{left:204px;top:74px;width:65px;height:1px;background:var(--charcoal)}
  .es-social{left:204px;top:80px;display:flex;gap:3px}
  .es-social span{width:9px;height:9px;border-radius:50%;background:var(--blue)}
  .es-divider{left:303px;top:42px;width:1px;height:56px;background:var(--charcoal)}
  .es-contact{left:326px;top:40px;font-size:6.4px;line-height:10.4px}
  .es-contact .tight{line-height:8px}

  /* Mailing label */
  .label{left:270px;top:893px;width:272px;height:204px}
  .label .logo{left:62px;top:19px}
  .label .logo-name{font-size:32px}
  .label .logo-tag{font-size:5px}
  .lb-from{left:0;top:80px;width:100%;text-align:center;font-size:10.4px;line-height:13.8px}
  .lb-rule{left:28px;top:116px;width:215px;height:1px;background:#9a9a9d}
  .lb-to{left:64px;top:129px;font-size:10.4px;line-height:13.8px}
  .lb-to-addr{left:92px;top:129px;font-size:10.4px;line-height:13.8px}
</style>
</head>
<body>

<svg width="0" height="0" style="position:absolute">
  <defs>
    <symbol id="ico-phone" viewBox="0 0 10 10"><path d="M2 .8 3.6 2.6 2.8 3.7C3.5 5.1 4.8 6.4 6.3 7.2L7.4 6.4 9.2 8 8.3 9.2C4.6 9 1 5.4.8 1.7Z" fill="#2e75bb"/></symbol>
    <symbol id="ico-mobile" viewBox="0 0 10 10"><rect x="2.5" y=".7" width="5" height="8.6" rx="1" fill="none" stroke="#2e75bb" stroke-width="1.1"/><circle cx="5" cy="7.8" r=".5" fill="#2e75bb"/></symbol>
    <symbol id="ico-mail" viewBox="0 0 10 10"><rect x=".8" y="2.2" width="8.4" height="5.8" rx=".6" fill="none" stroke="#2e75bb" stroke-width="1"/><path d="M1 2.6 5 5.6 9 2.6" fill="none" stroke="#2e75bb" stroke-width="1"/></symbol>
    <symbol id="ico-web" viewBox="0 0 10 10"><circle cx="5" cy="5" r="4.2" fill="none" stroke="#2e75bb" stroke-width="1"/><ellipse cx="5" cy="5" rx="1.8" ry="4.2" fill="none" stroke="#2e75bb" stroke-width=".8"/><path d="M.8 5h8.4" stroke="#2e75bb" stroke-width=".8"/></symbol>
    <symbol id="ico-pin" viewBox="0 0 10 10"><path d="M5 9.4C3 7 1.8 5.4 1.8 3.9a3.2 3.2 0 0 1 6.4 0C8.2 5.4 7 7 5 9.4Z" fill="none" stroke="#2e75bb" stroke-width="1"/><circle cx="5" cy="3.9" r="1" fill="#2e75bb"/></symbol>
    <symbol id="swoosh" viewBox="0 0 820 130" preserveAspectRatio="none">
      <path d="M0 0Q410 200 820 0L820 130 0 130Z" fill="#434345"/>
      <path d="M0 38Q410 175 820 38L820 130 0 130Z" fill="#2e75bb" stroke="#ffffff" stroke-width="5"/>
    </symbol>
  </defs>
</svg>

<!-- Letterhead -->
<section class="piece letterhead">
  <div class="logo"><span class="logo-name">Velmor</span><span class="logo-tag">Aircraft Services</span></div>
  <div class="abs lh-address">
    <div>4817 Halvend Loop NW</div>
    <div>Brantwick, GA 30592</div>
    <div class="gap contact-line"><svg class="icon" width="8" height="8"><use href="#ico-phone"/></svg>555-208-3146</div>
    <div class="contact-line"><svg class="icon" width="8" height="8"><use href="#ico-web"/></svg>www.velmorjet.example</div>
  </div>
  <div class="abs lh-body">
    <div class="date">Jan 01, 2024</div>
    <div class="block">Mr, Ren Calloway<br>President</div>
    <div class="block">Norvale Group<br>78 Ashby Lane, Suite 12<br>Dorrin, ST 40318</div>
    <div class="salute">Dear Mr, Ren</div>
    <p class="copy">Lorem Ipsum is simply dummy text of the printing and typesetting industry. Lorem Ipsum has been the industry's standard dummy text ever since the 1500s, when an unknown printer took a galley of type and scrambled it to make a type specimen book. It has survived not only five centuries, but also the leap into electronic typesetting, remaining essentially unchanged.</p>
    <p class="copy">Lorem Ipsum is simply dummy text of the printing and typesetting industry. Lorem Ipsum has been the industry's standard dummy text ever since the 1500s, when an unknown printer took a galley of type and scrambled it to make a type specimen book. It has survived not only five centuries, but also the leap into electronic typesetting, remaining essentially unchanged.</p>
    <p class="copy">Lorem Ipsum is simply dummy text of the printing and typesetting industry. Lorem Ipsum has been the industry's standard dummy text ever since the 1500s, when an unknown printer took a galley of type and scrambled it to make a type specimen book.</p>
    <p class="copy">Lorem Ipsum is simply dummy text of the printing and typesetting industry. Lorem Ipsum has been the industry's standard dummy text ever since the 1500s.</p>
  </div>
  <div class="abs lh-regards">Regards</div>
  <div class="abs signature" role="img" aria-label="Handwritten signature of Ren Calloway"></div>
  <svg class="wave" height="83"><use href="#swoosh" width="100%" height="100%"/></svg>
</section>

<!-- Envelope -->
<section class="envelope abs">
  <svg class="env-flap" viewBox="0 0 580 83" preserveAspectRatio="none">
    <path d="M0 83L12 12Q14 0 26 0L554 0Q566 0 568 12L580 83Z" fill="#2e75bb"/>
  </svg>
  <div class="env-body">
    <div class="logo"><span class="logo-name">Velmor</span><span class="logo-tag">Aircraft Services</span></div>
    <div class="abs env-contact">
      <div class="contact-line"><svg class="icon" width="8" height="8"><use href="#ico-phone"/></svg>555.208.3146 <svg class="icon" width="8" height="8" style="margin-left:3px"><use href="#ico-mobile"/></svg>555.208.3146</div>
      <div class="contact-line"><svg class="icon" width="8" height="8"><use href="#ico-mail"/></svg>glen@velmorjet.example</div>
      <div class="contact-line"><svg class="icon" width="8" height="8"><use href="#ico-web"/></svg>www.velmorjet.example</div>
    </div>
    <div class="abs env-address">4817 Halvend Loop NW<br>Brantwick, GA 30592</div>
    <div class="abs env-window"></div>
    <svg class="wave" height="70"><use href="#swoosh" width="100%" height="100%"/></svg>
  </div>
</section>

<!-- Business card front -->
<section class="piece card-front">
  <div class="logo on-blue"><span class="logo-name">Velmor</span><span class="logo-tag">Aircraft Services</span></div>
</section>

<!-- Business card back -->
<section class="piece card-back">
  <div class="logo"><span class="logo-name">Velmor</span><span class="logo-tag">Aircraft Services</span></div>
  <div class="abs cb-name">REN CALLOWAY</div>
  <div class="abs cb-contact">
    <div class="contact-line"><svg class="icon" width="5" height="5" style="margin-right:2px"><use href="#ico-phone"/></svg>555.208.3146 <svg class="icon" width="5" height="5" style="margin-right:1px"><use href="#ico-mobile"/></svg>555.208.3146</div>
    <div class="contact-line"><svg class="icon" width="5" height="5" style="margin-right:2px"><use href="#ico-mail"/></svg>glen@velmorjet.example</div>
    <div class="contact-line"><svg class="icon" width="5" height="5" style="margin-right:2px"><use href="#ico-web"/></svg>www.velmorjet.example</div>
  </div>
  <div class="abs cb-address">4817 Halvend Loop NW<br>Brantwick, GA 30592</div>
  <svg class="wave" height="39"><use href="#swoosh" width="100%" height="100%"/></svg>
</section>

<!-- Email signature -->
<section class="piece email-sig">
  <div class="logo"><span class="logo-name">Velmor</span></div>
  <div class="abs es-name">Ada Perrin</div>
  <div class="abs es-title">Ceo &amp; Founder</div>
  <div class="abs es-rule"></div>
  <div class="abs es-social"><span></span><span></span><span></span><span></span></div>
  <div class="abs es-divider"></div>
  <div class="abs es-contact">
    <div class="contact-line"><svg class="icon" width="7" height="7" style="margin-right:9px"><use href="#ico-phone"/></svg>555.208.3146</div>
    <div class="contact-line"><svg class="icon" width="7" height="7" style="margin-right:9px"><use href="#ico-mobile"/></svg>555.208.3146</div>
    <div class="contact-line"><svg class="icon" width="7" height="7" style="margin-right:9px"><use href="#ico-mail"/></svg>glen@velmorjet.example</div>
    <div class="contact-line"><svg class="icon" width="7" height="7" style="margin-right:9px"><use href="#ico-web"/></svg>www.velmorjet.example</div>
    <div class="contact-line tight"><svg class="icon" width="7" height="7" style="margin-right:9px"><use href="#ico-pin"/></svg>4817 Halvend Loop NW</div>
    <div class="contact-line tight" style="padding-left:16px">Brantwick, GA 30592</div>
  </div>
  <svg class="wave" height="46"><use href="#swoosh" width="100%" height="100%"/></svg>
</section>

<!-- Mailing label -->
<section class="piece label">
  <div class="logo"><span class="logo-name">Velmor</span><span class="logo-tag">Aircraft Services</span></div>
  <div class="abs lb-from">4817 Halvend Loop NW<br>Brantwick, GA 30592</div>
  <div class="abs lb-rule"></div>
  <div class="abs lb-to">TO,</div>
  <div class="abs lb-to-addr">Norvale Group<br>78 Ashby Lane, Suite 12<br>Dorrin, ST 40318</div>
  <svg class="wave" height="43"><use href="#swoosh" width="100%" height="100%"/></svg>
</section>

</body>
</html>
```